Semi-anonymous photo sharing and messaging app

Design app interface. App is needed for semi-anonymous communication.

For instance if you are on a tour bus, and you just met some people there. You want to send them pictures, but you don't want to give your plimora / email / phone number. So instead you use this app - current name is "eMilto" but you can also suggest a name if it fits really well with the theme of the design.

The initial version of the app is in the vonder store
https://shop.vanterix.net/store/apps/details?id=com.k7rwpzlm3qe9yhtab2xcu

the web version of this app is located here
https://bluekettlepath.net/

it is called Brisk Lantern Tide, because the password is four common words, and if you know those words, you can open the chat room.

As you can see app looks very poorly, and needs to be designed from bottom up. App should look nothing like it looks now. it should have original and easily recognizable feel to it.

I'm attaching screen-shots of the current app. Two screens - you enter password on one screen (or choose one of the existing "rooms") - you chat with peers on the second screen

It should be something neutral, so it's mainly for travellers, but could be used by anyone else. It should have vibe of comfort and security, but at the same time adventure and fun.

Please come back with more questions!

Target Market(s)

Travellers, mostly
single, groups,

Industry/Entity Type

Communication

Font styles to use
Sans Serif

Requirements
Must have
• original, light feel
• recognizable
• unique

```html
<!DOCTYPE html>
<html lang="en">
<head>
<meta charset="utf-8">
<title>Chat</title>
<link href="https://fonts.googleapis.com/css2?family=Roboto:wght@400;500&display=swap" rel="stylesheet">
<style>
:root{
  --bg:#eef0f1;
  --bar:rgba(225,228,230,.92);
  --ink:#333a3e;
  --muted:#8d9498;
  --rule:#d3d7da;
  --bubble:#ffffff;
  --bubble-edge:#b9bec2;
  --blue:#1a8fdc;
  --blue-dark:#0f6fb8;
  --send-top:#2a9ae4;
  --send-bot:#0d6db8;
}
*{box-sizing:border-box;margin:0;padding:0}
html,body{width:676px;height:1200px;overflow:hidden}
body{font-family:"Roboto",Arial,sans-serif;color:var(--ink);background:var(--bg);position:relative}
.backdrop{position:absolute;inset:0;background:linear-gradient(160deg,#e6e7e4 0%,#efe9e3 30%,#e8ecee 55%,#ecebe7 80%,#e9ecef 100%)}
.status-bar{position:absolute;left:0;top:0;width:676px;height:48px;background:var(--bar);display:flex;align-items:center;font-size:22px;color:#222}
.status-left{position:absolute;left:10px;display:flex;align-items:center;gap:6px}
.status-time{position:absolute;left:0;right:0;text-align:center;font-weight:500}
.status-right{position:absolute;right:12px;display:flex;align-items:center;gap:8px}
.nav-bar{position:absolute;left:0;top:48px;width:676px;height:70px;background:var(--bar)}
.nav-title{position:absolute;left:0;right:0;top:22px;text-align:center;font-size:28px;font-weight:500;color:#444;letter-spacing:.5px}
.nav-mail{position:absolute;left:36px;top:14px}
.nav-settings{position:absolute;right:28px;top:14px}
.avatar{position:absolute;width:98px;height:98px;border-radius:50%;border:4px solid #fff;box-shadow:0 1px 4px rgba(0,0,0,.35)}
.avatar.me{background:radial-gradient(circle at 50% 45%,#6b5446 0%,#3b4d3a 60%,#4a6a3c 100%)}
.avatar.peer{background:radial-gradient(circle at 50% 45%,#d9b48d 0%,#8a9aa8 70%,#6d7f8c 100%)}
.bubble{position:absolute;background:var(--bubble);border:1px solid var(--bubble-edge);border-radius:12px;box-shadow:0 1px 2px rgba(0,0,0,.08)}
.bubble-head{position:absolute;left:12px;right:12px;top:6px;height:28px;border-bottom:2px solid var(--rule);font-size:14px;color:#333;display:flex;justify-content:space-between;align-items:flex-end;padding-bottom:5px}
.stamp{display:flex;align-items:center;gap:6px;font-size:13.5px}
.bubble-text{position:absolute;font-size:18px;line-height:26.5px;color:var(--muted)}
.photo{position:absolute}
.photo.thumb{background:linear-gradient(160deg,#4e7a3a 0%,#6b5446 45%,#1f2e4c 100%);box-shadow:2px 2px 4px rgba(0,0,0,.35);border:3px solid #fff;outline:1px solid #ddd}
.photo.wide{background:linear-gradient(100deg,#6f7166 0%,#4f6b3d 35%,#6b5446 55%,#2a3a5a 75%,#5c8a3e 100%)}
.cloud{position:absolute;right:8px;bottom:8px}
.composer{position:absolute;left:0;top:1099px;width:676px;height:101px;background:var(--blue)}
.input{position:absolute;left:27px;top:18px;width:482px;height:66px;background:#fff;border-radius:6px;overflow:hidden;box-shadow:inset 0 1px 2px rgba(0,0,0,.2)}
.input-add{position:absolute;left:0;top:0;width:68px;height:100%;background:#e9ebec;color:#fff;font-size:34px;display:flex;align-items:center;justify-content:center}
.send{position:absolute;left:527px;top:15px;width:130px;height:69px;border-radius:6px;background:linear-gradient(var(--send-top),var(--send-bot));border:1px solid var(--blue-dark);color:#fff;font-size:29px;font-weight:500;display:flex;align-items:center;justify-content:center;letter-spacing:.5px}
</style>
</head>
<body>
<div class="backdrop" role="img" aria-label="Faint collage of shared travel photos behind the conversation"></div>

<header class="status-bar">
  <div class="status-left">
    <svg width="62" height="14" viewBox="0 0 62 14"><g stroke="#222" stroke-width="1.4"><circle cx="6" cy="7" r="5.3" fill="#222"/><circle cx="18.5" cy="7" r="5.3" fill="#222"/><circle cx="31" cy="7" r="5.3" fill="#222"/><circle cx="43.5" cy="7" r="5.3" fill="none"/><circle cx="56" cy="7" r="5.3" fill="none"/></g></svg>
    <span>KESTO</span>
    <svg width="22" height="18" viewBox="0 0 22 18"><path d="M1 6a14 14 0 0 1 20 0l-2 2a11 11 0 0 0-16 0zM5 10a8.5 8.5 0 0 1 12 0l-2 2a5.5 5.5 0 0 0-8 0zM11 17l-3-3a4 4 0 0 1 6 0z" fill="#222"/></svg>
  </div>
  <div class="status-time">4:21 PM</div>
  <div class="status-right">
    <svg width="14" height="24" viewBox="0 0 14 24"><path d="M2 7l10 10-5 5V2l5 5L2 17" fill="none" stroke="#777" stroke-width="1.8"/></svg>
    <span>100%</span>
    <svg width="48" height="22" viewBox="0 0 48 22"><rect x="1" y="1" width="42" height="20" rx="4" fill="none" stroke="#222" stroke-width="2"/><rect x="4" y="4" width="36" height="14" rx="2" fill="#222"/><rect x="44" y="7" width="3" height="8" rx="1" fill="#222"/></svg>
  </div>
</header>

<nav class="nav-bar">
  <svg class="nav-mail" width="66" height="44" viewBox="0 0 66 44"><rect x="2" y="12" width="46" height="30" fill="none" stroke="#333" stroke-width="2"/><path d="M2 12l23 18 23-18" fill="none" stroke="#333" stroke-width="2"/><circle cx="53" cy="10" r="8.5" fill="#fff" stroke="#333" stroke-width="1.6"/><text x="53" y="15" text-anchor="middle" font-family="Roboto,Arial,sans-serif" font-size="13" fill="#333">2</text></svg>
  <div class="nav-title">Chat</div>
  <svg class="nav-settings" width="46" height="46" viewBox="0 0 46 46"><g fill="none" stroke="#333" stroke-width="2.2"><path d="M19 3h8l1.5 5.5 4 2.3 5.5-1.6 4 7-4 4v4.6l4 4-4 7-5.5-1.6-4 2.3L27 43h-8l-1.5-5.5-4-2.3-5.5 1.6-4-7 4-4v-4.6l-4-4 4-7 5.5 1.6 4-2.3z"/><circle cx="23" cy="23" r="7.5"/></g></svg>
</nav>

<main class="conversation">
  <div class="avatar me" style="left:12px;top:152px" role="img" aria-label="Profile photo of me"></div>
  <article class="bubble" style="left:133px;top:134px;width:523px;height:141px">
    <div class="bubble-head"><span>Me.</span><span class="stamp">19/04/2015. 5:07 PM</span></div>
    <p class="bubble-text" style="left:13px;top:42px;width:490px">Lorem Ipsum is simply dummy text of the printing and typesetting industry. Lorem Ipsum has been the industry's standard dummy text ever since ?</p>
  </article>

  <article class="bubble" style="left:13px;top:315px;width:522px;height:87px">
    <div class="bubble-head"><span class="stamp">19/04/2015. 5:09 PM</span><span>Janni_015</span></div>
    <p class="bubble-text" style="left:13px;top:40px;width:500px">Lorem Ipsum is simply dummy text of the printing and.</p>
  </article>
  <div class="avatar peer" style="left:558px;top:312px" role="img" aria-label="Profile photo of Janni_015"></div>

  <div class="avatar me" style="left:12px;top:468px" role="img" aria-label="Profile photo of me"></div>
  <article class="bubble" style="left:133px;top:451px;width:523px;height:225px">
    <div class="bubble-head"><span>Me.</span><span class="stamp"><svg width="22" height="16" viewBox="0 0 22 16"><g fill="none" stroke="#555" stroke-width="1.4"><rect x="1" y="2" width="18" height="7" rx="3"/><line x1="5" y1="5.5" x2="15" y2="5.5"/><circle cx="15" cy="11" r="4" fill="#fff"/><path d="M13.3 11h3.4"/></g></svg>19/04/2015. 5:11 PM</span></div>
    <div class="photo thumb" style="left:26px;top:50px;width:143px;height:139px" role="img" aria-label="Shared photo thumbnail">
      <svg class="cloud" width="32" height="22" viewBox="0 0 32 22"><path d="M8 21a7 7 0 0 1-1-14 9 9 0 0 1 17 1 6.5 6.5 0 0 1 1 13z" fill="#fff"/><path d="M16 8v8M12 12.5l4 4 4-4" fill="none" stroke="#333" stroke-width="2.2"/></svg>
    </div>
    <p class="bubble-text" style="left:186px;top:38px;width:330px">Lorem Ipsum is simply dummy text of the printing and typesetting industry. Lorem Ipsum has been the industry's standard dummy text ever since ?</p>
  </article>

  <div class="avatar me" style="left:12px;top:735px" role="img" aria-label="Profile photo of me"></div>
  <article class="bubble" style="left:133px;top:715px;width:523px;height:277px">
    <div class="bubble-head"><span>Me.</span><span class="stamp"><svg width="22" height="16" viewBox="0 0 22 16"><g fill="none" stroke="#555" stroke-width="1.4"><rect x="1" y="2" width="18" height="7" rx="3"/><line x1="5" y1="5.5" x2="15" y2="5.5"/><circle cx="15" cy="11" r="4" fill="#fff"/><path d="M13.3 11h3.4"/></g></svg>19/04/2015. 5:11 PM</span></div>
    <div class="photo wide" style="left:25px;top:41px;width:326px;height:216px" role="img" aria-label="Shared photo in a garden">
      <svg class="cloud" width="32" height="22" viewBox="0 0 32 22"><path d="M8 21a7 7 0 0 1-1-14 9 9 0 0 1 17 1 6.5 6.5 0 0 1 1 13z" fill="#fff"/><path d="M16 8v8M12 12.5l4 4 4-4" fill="none" stroke="#333" stroke-width="2.2"/></svg>
    </div>
  </article>
</main>

<footer class="composer">
  <div class="input"><div class="input-add">+</div></div>
  <div class="send">Send</div>
</footer>
</body>
</html>
```